Quellmont Haus National Website

We need a website to match our Logo. We will be selling american made vapeing Oils, batteries, Cartomizers, Clearomizers. We have a wharehouse location with couches, TVs streaming clipora, vending machine, and the worlds first flavor mixing bar. We have the lowest priced high grade oils. We will send pictures of the location. Relaxed atmoshpere and no lines for purchase. VIP cards for regulars.

(PLEASE KNOW THAT THE LOGO IS THE UPPER RIGHT LOGO ONLY OF THE FOUR ON THE FILE I ATTACHED)
Updates

Keep in mind we are are only looking for concept and a non coded website

Please know that we are looking for a non coded website

Industry/Entity Type

Purchase

Requirements
Must have
• Online cart, Blog,

```html
<!DOCTYPE html>
<html lang="en">
<head>
<meta charset="utf-8">
<title>Quellmont Haus</title>
<link href="https://fonts.googleapis.com/css2?family=Open+Sans:wght@400;600&display=swap" rel="stylesheet">
<style>
:root{
  --green:#6cbf3c;
  --green-dark:#57a82b;
  --green-text:#4f9e23;
  --black:#000;
  --ink:#333;
  --muted:#666;
  --panel:#f2f1f1;
  --band:#f1f1f1;
  --white:#fff;
}
*{margin:0;padding:0;box-sizing:border-box}
html,body{width:1055px;height:1200px;overflow:hidden}
body{position:relative;font-family:"Open Sans",Arial,sans-serif;background:var(--white);color:var(--ink)}
.abs{position:absolute}

.site-header{position:absolute;left:0;top:0;width:1055px;height:86px;background:var(--black);border-top:3px solid var(--green)}
.brand{position:absolute;left:137px;top:26px;display:flex;align-items:center;gap:8px;color:var(--green);font-size:26px;font-weight:400;letter-spacing:-.5px;white-space:nowrap}
.brand-mark{width:12px;height:12px;background:var(--green);border-radius:50%}
.main-nav{position:absolute;top:34px;left:0;font-size:13px;font-weight:600;color:var(--white)}
.main-nav span{position:absolute;white-space:nowrap}
.main-nav .active{color:var(--green)}
.cart-button{position:absolute;left:788px;top:23px;width:123px;height:36px;background:var(--green);border-radius:2px;color:#222;font-size:13px;font-weight:600;display:flex;align-items:center;justify-content:center;gap:14px;white-space:nowrap}

.hero{position:absolute;left:0;top:86px;width:1055px;height:380px;background:radial-gradient(ellipse at 55% 40%,#a08a6e 0%,#6b5a45 35%,#3a3026 70%,#1e1a15 100%)}
.hero-arrow{position:absolute;top:165px;width:42px;height:43px;background:rgba(0,0,0,.6);display:flex;align-items:center;justify-content:center}
.hero-caption{position:absolute;height:38px;padding:0 16px 0 0;font-size:22px;line-height:38px;color:var(--white);display:flex;align-items:center;justify-content:flex-end;white-space:nowrap;overflow:hidden}
.cap-dark{background:#000;top:132px;left:215px;width:140px}
.cap-green{background:var(--green);color:#1a1a1a}
.cap-taste{top:173px;left:180px;width:175px}
.cap-product{top:214px;left:137px;width:218px}

.product-card{position:absolute;top:507px;width:243px;height:220px;background:var(--panel);border-top:4px solid var(--green)}
.product-photo{position:absolute;left:15px;top:11px;width:212px;height:94px}
.product-title{position:absolute;left:15px;top:117px;font-size:15px;font-weight:400;color:#222;white-space:nowrap}
.product-desc{position:absolute;left:15px;top:141px;width:220px;font-size:10.5px;line-height:14px;color:var(--muted)}
.read-btn{position:absolute;left:15px;top:182px;width:66px;height:22px;background:var(--green-dark);color:var(--white);font-size:10.5px;font-weight:600;display:flex;align-items:center;justify-content:center;white-space:nowrap}
.price{position:absolute;right:19px;top:184px;display:flex;align-items:center;gap:8px;font-size:13px;color:#333;white-space:nowrap}

.more-link{position:absolute;left:0;width:1055px;top:742px;text-align:center;font-size:11.5px;color:var(--green-text)}

.blog-panel{position:absolute;left:137px;top:789px;width:508px;height:232px;background:var(--panel)}
.section-title{font-size:15px;font-weight:400;color:#222;white-space:nowrap}
.section-title b{font-weight:400;color:var(--green-text)}
.blog-rule{position:absolute;left:15px;top:44px;width:473px;height:1px;background:#d6d6d6}
.blog-post{position:absolute;top:56px;width:215px}
.blog-photo{width:209px;height:84px}
.blog-text{margin-top:10px;font-size:10px;line-height:14px;color:#333;letter-spacing:-.05px}
.blog-more{margin-top:10px;font-size:11.5px;color:var(--green-text)}

.features{position:absolute;left:666px;top:795px;width:245px}
.features .rule{border-top:1px dashed var(--green);margin-top:8px}
.features p{font-size:10.5px;line-height:16px;color:#333;margin:8px 0 0 1px}
.feature{display:flex;align-items:center;gap:7px;height:29px;font-size:10.5px;color:#333;border-bottom:1px dashed var(--green);padding-left:2px;white-space:nowrap}
.feature:last-child{border-bottom:none}

.contact-band{position:absolute;left:0;top:1062px;width:1055px;height:50px;background:var(--band);border-top:1px solid #ddd;display:flex;justify-content:center;align-items:center;gap:50px;font-size:13px;color:#888;white-space:nowrap}
.contact-band span b{font-weight:400;color:#222}

.site-footer{position:absolute;left:0;top:1112px;width:1055px;height:88px;background:#0a0a0a}
.footer-nav{position:absolute;left:0;width:1030px;top:29px;text-align:center;font-size:10.5px;color:#ccc;white-space:nowrap}
.footer-nav span{margin:0 9px}
.footer-nav .active{color:var(--green)}
.copyright{position:absolute;left:0;width:1030px;top:47px;text-align:center;font-size:10.5px;color:#ccc}
.social{position:absolute;left:760px;top:37px;display:flex;gap:10px;font-size:10px;color:#bbb;white-space:nowrap}
</style>
</head>
<body>

<header class="site-header">
  <div class="brand"><span class="brand-mark"></span>Quellmont Haus</div>
  <nav class="main-nav">
    <span class="active" style="left:481px">Home</span>
    <span style="left:543px">Our Products</span>
    <span style="left:648px">Blog</span>
    <span style="left:700px">Contact Us</span>
  </nav>
  <div class="cart-button"><span>Cart : 0</span><span>| $ 0.00</span></div>
</header>

<section class="hero" role="img" aria-label="Photo of a tattooed man exhaling vapour from a vaporizer in a dim lounge">
  <div class="hero-arrow" style="left:0"><svg width="12" height="20" viewBox="0 0 12 20"><path d="M10 2 2 10l8 8" fill="none" stroke="#ddd" stroke-width="2"/></svg></div>
  <div class="hero-arrow" style="left:1013px"><svg width="12" height="20" viewBox="0 0 12 20"><path d="M2 2l8 8-8 8" fill="none" stroke="#ddd" stroke-width="2"/></svg></div>
  <div class="hero-caption cap-dark">Welcome!</div>
  <div class="hero-caption cap-green cap-taste">Get a taste of</div>
  <div class="hero-caption cap-green cap-product">American product</div>
</section>

<article class="product-card" style="left:137px">
  <div class="product-photo" role="img" aria-label="Blue glass hookah on a pale teal background" style="background:linear-gradient(135deg,#b7cbc6,#8aa7a2)"></div>
  <h3 class="product-title">Vapeing Oils</h3>
  <p class="product-desc">Lorem ipsum dolor sit amet, consectetur adipisicing elit, sed do eiusmod tempor.</p>
  <div class="read-btn">Read More</div>
  <div class="price">$ 50 <svg width="26" height="20" viewBox="0 0 26 20"><path d="M1 2h4l3 12h14l3-9H7" fill="none" stroke="#5cb334" stroke-width="2"/><path d="M8 8h15M9 11h13" stroke="#5cb334" stroke-width="1.5"/><circle cx="10" cy="18" r="1.6" fill="#5cb334"/><circle cx="20" cy="18" r="1.6" fill="#5cb334"/></svg></div>
</article>

<article class="product-card" style="left:401px">
  <div class="product-photo" role="img" aria-label="Still life of a wine glass, pewter cup, lemon and nuts" style="background:linear-gradient(135deg,#3f3424,#7a5f36 50%,#2b2418)"></div>
  <h3 class="product-title">Flavor mixing bar</h3>
  <p class="product-desc">Lorem ipsum dolor sit amet, consectetur adipisicing elit, sed do eiusmod tempor.</p>
  <div class="read-btn">Read More</div>
  <div class="price">$ 45 <svg width="26" height="20" viewBox="0 0 26 20"><path d="M1 2h4l3 12h14l3-9H7" fill="none" stroke="#5cb334" stroke-width="2"/><path d="M8 8h15M9 11h13" stroke="#5cb334" stroke-width="1.5"/><circle cx="10" cy="18" r="1.6" fill="#5cb334"/><circle cx="20" cy="18" r="1.6" fill="#5cb334"/></svg></div>
</article>

<article class="product-card" style="left:667px">
  <div class="product-photo" role="img" aria-label="Glass cup of amber tea with green leaves and flowers" style="background:linear-gradient(160deg,#f3efe9 30%,#d89a4a 60%,#7e9c3a)"></div>
  <h3 class="product-title">High grade oils</h3>
  <p class="product-desc">Lorem ipsum dolor sit amet, consectetur adipisicing elit, sed do eiusmod tempor.</p>
  <div class="read-btn">Read More</div>
  <div class="price">$ 30 <svg width="26" height="20" viewBox="0 0 26 20"><path d="M1 2h4l3 12h14l3-9H7" fill="none" stroke="#5cb334" stroke-width="2"/><path d="M8 8h15M9 11h13" stroke="#5cb334" stroke-width="1.5"/><circle cx="10" cy="18" r="1.6" fill="#5cb334"/><circle cx="20" cy="18" r="1.6" fill="#5cb334"/></svg></div>
</article>

<div class="more-link">More Product &gt;&gt;</div>

<section class="blog-panel">
  <h2 class="section-title abs" style="left:15px;top:15px"><b>Blog</b> with us</h2>
  <div class="blog-rule"></div>
  <div class="blog-post" style="left:15px">
    <div class="blog-photo" role="img" aria-label="Warmly lit lounge bar with round pendant lamps" style="background:linear-gradient(135deg,#5a2a1e,#b07a3a 45%,#3a1a20)"></div>
    <p class="blog-text">Lorem ipsum dolor sit amet, consectetur adipisicing elit, sed do eiusmod tempor incididunt ut labore et dolore magna aliqua.</p>
    <p class="blog-more">Read More...</p>
  </div>
  <div class="blog-post" style="left:264px">
    <div class="blog-photo" role="img" aria-label="Man exhaling vapour in a smoky room" style="background:radial-gradient(ellipse at 55% 45%,#9c866a,#3a3026 80%)"></div>
    <p class="blog-text">Lorem ipsum dolor sit amet, consectetur adipisicing elit, sed do eiusmod tempor incididunt ut labore et dolore magna aliqua.</p>
    <p class="blog-more">Read More...</p>
  </div>
</section>

<aside class="features">
  <h2 class="section-title"><b>Unique</b> features</h2>
  <div class="rule"></div>
  <p>Read our unique features that will insist&nbsp; you to come once to our shop to try our products.</p>
  <div style="margin-top:4px">
    <div class="feature"><svg width="8" height="7" viewBox="0 0 8 7"><path d="M1 3.5 3 5.5 7 1" fill="none" stroke="#6cbf3c" stroke-width="1.6"/></svg>Worlds first flavor mixing bar</div>
    <div class="feature"><svg width="8" height="7" viewBox="0 0 8 7"><path d="M1 3.5 3 5.5 7 1" fill="none" stroke="#6cbf3c" stroke-width="1.6"/></svg>Lowest priced high grade oils</div>
    <div class="feature"><svg width="8" height="7" viewBox="0 0 8 7"><path d="M1 3.5 3 5.5 7 1" fill="none" stroke="#6cbf3c" stroke-width="1.6"/></svg>Relaxed atmoshpere</div>
    <div class="feature"><svg width="8" height="7" viewBox="0 0 8 7"><path d="M1 3.5 3 5.5 7 1" fill="none" stroke="#6cbf3c" stroke-width="1.6"/></svg>No lines for purchase</div>
    <div class="feature"><svg width="8" height="7" viewBox="0 0 8 7"><path d="M1 3.5 3 5.5 7 1" fill="none" stroke="#6cbf3c" stroke-width="1.6"/></svg>VIP cards for regulars</div>
  </div>
</aside>

<section class="contact-band">
  <span>Call us for any queries : <b>081 - 555 - 0142</b></span>
  <span>Email is : <b>hello@quellmonthaus.com</b></span>
</section>

<footer class="site-footer">
  <div class="footer-nav"><span class="active">Home</span><span>Our Products</span><span>Blog</span><span>Contact Us</span></div>
  <div class="copyright">Copyright@2013, quellmont haus</div>
  <div class="social"><span>clipora</span><span>Chirpline</span></div>
</footer>

</body>
</html>
```